Bourbon Lantern is a speakeasy whiskey and cigar website needing fresh look for product sales

This is a new company just starting out that will be Design needs to be modern edge of prohibition of the 1920's and the speakeasies that were created from them. Needs to include the moonshine runners, stills and whiskey. Also needs to have the sophistication of a speakeasy where gentlemen and now women go to sit in luxury leather chairs with their whiskey and cigar. Lastly my website will not be selling alcohol or cigars. Just higher end accessories and furniture designs in the Bourbon Lantern store that will help the consumer feel like they are back in time while sitting in the comfort of their own speakeasy.

I will attach my current logo but I am open to suggestions to better suit my vision. I do have photos of products that have been purchased to put on website. I am leaving the designs of actual website itself to the designer.

Target Market(s)

21 yrs +; home owners; mature audience; redesign room; cigar accessories; liquor accessories

Industry/Entity Type

home bars, liquor accessories, cigar accessories

Coding

Coded - Design and coding required

Number of Pages Required

1 page

Font styles to use
Serif
Decorative
Script

Colors

Designer to choose colors to be used in the design.

Requirements
Must have
• key words for search engines, eye catching designs matching key words, links to online store and social media
Nice to have
• logo, mixture of retro/old feel with modern day twist; speakeasy/moonshine runners with luxury and class
Should not have
• nudity, XXX, racism

```html
<!DOCTYPE html>
<html lang="en">
<head>
<meta charset="utf-8">
<title>Bourbon Lantern – Whiskey Accessories</title>
<link href="https://fonts.googleapis.com/css2?family=Libre+Caslon+Text:wght@400;700&family=Montserrat:wght@400;500;600;700&display=swap" rel="stylesheet">
<style>
:root{
  --ink:#0b0b0b;
  --bg-top:#3a393a;
  --bg-bot:#5a5455;
  --rose:#d9bcad;
  --rose-deep:#c39a88;
  --text:#f4eeea;
  --muted:#d8d0cc;
  --card:#232323;
  --gold:#f1b51c;
  --footer:#9d6a56;
  --footer-deep:#6e4637;
  --serif:"Libre Caslon Text", Georgia, serif;
  --sans:"Montserrat", Arial, sans-serif;
}
*{box-sizing:border-box;margin:0;padding:0}
html,body{width:1200px;height:3888px;overflow:hidden}
body{position:relative;background:var(--bg-top);font-family:var(--serif);color:var(--text)}
.abs{position:absolute}
a{color:inherit;text-decoration:none}

/* header */
.site-header{position:absolute;left:0;top:0;width:1200px;height:88px;background:var(--ink);z-index:5}
.brand-badge{position:absolute;left:114px;top:-18px;width:156px;height:162px;border-radius:0 0 80px 80px;background:var(--ink);border-bottom:5px solid var(--rose);z-index:6;display:flex;align-items:center;justify-content:center}
.brand-badge span{font-family:var(--serif);font-size:17px;color:var(--rose);text-align:center;line-height:1.25;margin-top:14px}
.main-nav{position:absolute;top:32px;left:0;font-family:var(--sans);font-size:15px;color:var(--text)}
.main-nav a{position:absolute;white-space:nowrap}
.main-nav .active{color:var(--rose);font-weight:600}
.nav-icons svg{position:absolute;top:28px}

/* hero */
.hero{position:absolute;left:0;top:88px;width:1200px;height:473px;overflow:hidden}
.hero-photo{position:absolute;inset:0;background:linear-gradient(100deg,#2a160e 0%,#4a2718 45%,#6b3a22 70%,#3a2014 100%)}
.hero-shade{position:absolute;inset:0;background:linear-gradient(90deg,rgba(0,0,0,.45),rgba(0,0,0,0) 65%)}
.hero-eyebrow{left:113px;top:106px;font-size:21px;line-height:28px;display:flex;align-items:center;gap:18px;white-space:nowrap}
.hero-eyebrow i{display:block;width:24px;height:4px;background:var(--rose)}
.hero-title{left:113px;top:150px;font-weight:400;font-size:42px;line-height:48px;white-space:nowrap}
.hero-title em,.section-title em{font-style:normal;color:var(--rose)}
.hero-text{left:113px;top:274px;font-size:16.5px;line-height:24px;width:580px}
.btn{position:absolute;background:var(--rose);color:#2a1d18;font-family:var(--serif);font-size:17px;border-radius:4px;display:flex;align-items:center;justify-content:center}

/* sections */
.section{position:absolute;left:0;width:1200px}
.section-title{position:absolute;left:0;width:1200px;text-align:center;font-weight:400;font-size:41px}
.section-lead{position:absolute;left:0;width:1200px;text-align:center;font-size:17px;line-height:26px;color:var(--muted)}
.products{top:561px;height:784px;background:radial-gradient(ellipse at 50% 40%,#4f4b4c,#363435 80%)}
.product-card{position:absolute;top:243px;width:291px}
.product-photo{width:291px;height:335px;border-radius:3px;position:relative;overflow:hidden}
.sale-tag{position:absolute;left:18px;top:24px;background:#d6b5a4;color:#3a2a22;font-size:15px;padding:2px 8px}
.wish{position:absolute;right:16px;top:20px;width:34px;height:34px;border-radius:50%;background:#8c8686;display:flex;align-items:center;justify-content:center}
.select-bar{position:absolute;left:0;bottom:0;width:100%;height:48px;background:var(--rose);color:#1e1612;display:flex;align-items:center;justify-content:center;gap:12px;font-size:16px}
.product-name{margin-top:18px;font-size:22px;color:var(--rose)}
.product-desc{margin-top:6px;font-family:var(--sans);font-size:13px;line-height:18px;color:var(--muted)}
.price-row{margin-top:10px;display:flex;justify-content:space-between;align-items:center}
.price{font-family:var(--sans);font-weight:700;font-size:18px}
.stars{color:var(--gold);font-size:14px;letter-spacing:1px;font-family:var(--sans)}
.arrow{position:absolute;top:362px;width:64px;height:64px;border-radius:50%;display:flex;align-items:center;justify-content:center;box-shadow:0 4px 10px rgba(0,0,0,.3)}

.about{top:1345px;height:532px;background:linear-gradient(90deg,#2e2520,#4a3e37 50%,#2f2620)}
.about h2{left:110px;top:112px;font-weight:400;font-size:42px}
.about p{left:110px;width:422px;font-size:15.5px;line-height:24px;color:var(--muted);text-align:justify}
.frame{position:absolute;border:3px solid #d9d0cc}

.accessories{top:1877px;height:720px;background:linear-gradient(180deg,#3a393a,#555051 60%,#4a4647)}
.acc-card{position:absolute;top:252px;width:219px}
.acc-photo{width:219px;height:223px;background:var(--card);border-radius:3px}
.acc-card .stars{font-size:12px;margin-top:18px;display:block}
.acc-name{font-size:19px;color:var(--muted);margin-top:2px}
.acc-price{font-family:var(--sans);font-weight:700;font-size:16px;margin-top:6px}

.video{top:2597px;height:403px}
.video-photo{position:absolute;inset:0;background:linear-gradient(180deg,#2b1a10 0%,#5b3a1f 45%,#8a5e2c 75%,#4a2d16 100%)}
.video h2{position:absolute;left:0;width:1200px;top:160px;text-align:center;font-weight:400;font-size:44px;text-shadow:0 2px 6px rgba(0,0,0,.6)}
.play{position:absolute;left:564px;top:233px;width:70px;height:70px;border-radius:50%;background:#fff;display:flex;align-items:center;justify-content:center}

.blog{top:3000px;height:629px;background:linear-gradient(180deg,#4a4647,#3d3b3c)}
.post{position:absolute;top:232px;width:300px}
.post-photo{width:300px;height:178px}
.post-cat{margin-top:34px;font-size:14px;color:var(--muted)}
.post-title{margin-top:18px;font-size:18px;line-height:24px}
.post-meta{margin-top:12px;font-size:12px;color:#a9a1a0}

.site-footer{top:3629px;height:259px;background:var(--footer)}
.footer-badge{position:absolute;left:531px;top:20px;width:136px;height:136px;border-radius:50%;border:3px solid #f1e3dc;display:flex;align-items:center;justify-content:center;text-align:center;font-size:17px;line-height:1.25;color:#fff}
.footer-nav a{position:absolute;top:162px;font-size:20px;color:#fff}
.copyright{position:absolute;left:0;top:211px;width:1200px;height:48px;background:var(--footer-deep);text-align:center;line-height:48px;font-family:var(--sans);font-size:13px;color:#d6c0b6}
</style>
</head>
<body>

<header class="site-header">
  <nav class="main-nav">
    <a class="active" style="left:361px">Home</a>
    <a style="left:439px">About Us</a>
    <a style="left:540px">Shop</a>
    <a style="left:611px">Accessories</a>
    <a style="left:729px">Blog</a>
    <a style="left:795px">Contact Us</a>
  </nav>
  <div class="nav-icons">
    <svg style="left:966px" width="34" height="32" viewBox="0 0 34 32" fill="none" stroke="#fff" stroke-width="2"><path d="M3 4h4l3 14h14l3-10H9"/><circle cx="24" cy="24" r="7" fill="var(--rose)" stroke="none"/><text x="24" y="28" font-size="10" text-anchor="middle" fill="#111" stroke="none" font-family="Montserrat">0</text></svg>
    <svg style="left:1017px" width="26" height="26" viewBox="0 0 26 26" fill="none" stroke="#fff" stroke-width="2.4"><circle cx="11" cy="11" r="8"/><path d="M17 17l6 6"/></svg>
    <svg style="left:1066px" width="22" height="22" viewBox="0 0 22 22" fill="#fff"><circle cx="3" cy="3" r="2.4"/><circle cx="11" cy="3" r="2.4"/><circle cx="19" cy="3" r="2.4"/><circle cx="3" cy="11" r="2.4"/><circle cx="11" cy="11" r="2.4"/><circle cx="19" cy="11" r="2.4"/><circle cx="3" cy="19" r="2.4"/><circle cx="11" cy="19" r="2.4"/><circle cx="19" cy="19" r="2.4"/></svg>
  </div>
</header>
<div class="brand-badge"><span>Bourbon<br>Lantern</span></div>

<section class="hero">
  <div class="hero-photo" role="img" aria-label="Warm wood-panelled speakeasy bar with taps, bottles and leather stools"></div>
  <div class="hero-shade"></div>
  <div class="abs hero-eyebrow"><i></i>Try our world-class whiskies</div>
  <h1 class="abs hero-title">Discover Top<br><em>Whiskey Accessories</em></h1>
  <p class="abs hero-text">Lorem ipsum dolor sit amet, consectetur adipiscing elit, sed do eiusmod incididunt ut labore et dolore magna aliqua.</p>
  <a class="btn" style="left:113px;top:337px;width:136px;height:33px">Get Started</a>
</section>

<section class="section products">
  <h2 class="section-title" style="top:80px">Popular <em>Products</em></h2>
  <p class="section-lead" style="top:148px">Lorem ipsum dolor sit amet, consectetur adipiscing elit,<br>sed do eiusmod tempor incididunt ut labore et dolore magna aliqua quis ipsum suspendisse ultrices gravida.</p>

  <div class="product-card" style="left:110px">
    <div class="product-photo" role="img" aria-label="Red lounge room with a green leather curved sofa" style="background:linear-gradient(180deg,#7a1d14,#b23a22 40%,#1f7a55 75%,#0f4a34)">
      <span class="sale-tag">-16%</span>
      <span class="wish"><svg width="18" height="16" viewBox="0 0 18 16" fill="none" stroke="#fff" stroke-width="1.6"><path d="M9 15S1 10 1 5a4 4 0 0 1 8-1 4 4 0 0 1 8 1c0 5-8 10-8 10z"/></svg></span>
    </div>
    <div class="product-name">Scotch Whisky</div>
    <div class="product-desc">Lorem ipsum dolor<br>sit amet, consectetur adipiscing elit, sed</div>
    <div class="price-row"><span class="price">$64.00</span><span class="stars">★★★★☆</span></div>
  </div>

  <div class="product-card" style="left:453px">
    <div class="product-photo" role="img" aria-label="Round wooden bar table on a black pedestal" style="background:radial-gradient(circle at 50% 45%,#4a4040,#222 70%)">
      <span class="sale-tag">-16%</span>
      <span class="wish"><svg width="18" height="16" viewBox="0 0 18 16" fill="none" stroke="#fff" stroke-width="1.6"><path d="M9 15S1 10 1 5a4 4 0 0 1 8-1 4 4 0 0 1 8 1c0 5-8 10-8 10z"/></svg></span>
    </div>
    <div class="product-name">Irish Whiskey</div>
    <div class="product-desc">Lorem ipsum dolor<br>sit amet, consectetur adipiscing elit, sed</div>
    <div class="price-row"><span class="price">$64.00</span><span class="stars">★★★★☆</span></div>
  </div>

  <div class="product-card" style="left:797px">
    <div class="product-photo" role="img" aria-label="Cream upholstered armchair on wooden legs" style="background:radial-gradient(circle at 50% 40%,#6a6566,#3f3c3d 75%)">
      <span class="sale-tag">-16%</span>
      <span class="wish"><svg width="18" height="16" viewBox="0 0 18 16" fill="none" stroke="#fff" stroke-width="1.6"><path d="M9 15S1 10 1 5a4 4 0 0 1 8-1 4 4 0 0 1 8 1c0 5-8 10-8 10z"/></svg></span>
      <div class="select-bar"><svg width="18" height="16" viewBox="0 0 18 16" fill="#111"><path d="M0 1h3l3 9h9l3-7H5l-.6-2H0z"/><circle cx="7" cy="14" r="1.6"/><circle cx="14" cy="14" r="1.6"/></svg>Select Option</div>
    </div>
    <div class="product-name">American Whiskey</div>
    <div class="product-desc">Lorem ipsum dolor<br>sit amet, consectetur adipiscing elit, sed</div>
    <div class="price-row"><span class="price">$64.00</span><span class="stars">★★★★☆</span></div>
  </div>

  <span class="arrow" style="left:63px;background:#fff"><svg width="20" height="30" viewBox="0 0 20 30" fill="none" stroke="#111" stroke-width="3.5"><path d="M15 3L4 15l11 12"/></svg></span>
  <span class="arrow" style="left:1071px;background:var(--rose)"><svg width="20" height="30" viewBox="0 0 20 30" fill="none" stroke="#fff" stroke-width="3.5"><path d="M5 3l11 12L5 27"/></svg></span>
</section>

<section class="section about" aria-label="About">
  <div class="abs" role="img" aria-label="Dark wood plank background" style="inset:0;background:repeating-linear-gradient(90deg,rgba(0,0,0,.12) 0 2px,transparent 2px 120px)"></div>
  <h2 class="abs">About <span style="color:var(--rose)">Bourbon Lantern</span></h2>
  <p class="abs" style="top:184px">Sed ut perspiciatis unde omnis iste natus error sit voluptatem accusantium doloremque laudantium, totam rem aperiam, eaque ipsa quae ab illo inventore veritatis et quasi architecto beatae vitae dicta sunt explicabo.</p>
  <p class="abs" style="top:289px">Nemo enim ipsam voluptatem quia voluptas sit aspernatur aut odit aut fugit, sed quia consequuntur magni dolores eos qui ratione voluptatem sequi nesciunt.</p>
  <a class="btn" style="left:110px;top:377px;width:136px;height:33px">Read More</a>
  <div class="frame" role="img" aria-label="Row of brass beer taps in a dim bar" style="left:726px;top:84px;width:364px;height:296px;background:linear-gradient(135deg,#2a1a10,#8a5a2a 45%,#3a2416)"></div>
  <div class="frame" role="img" aria-label="Modern dark bar counter with stools" style="left:569px;top:235px;width:228px;height:208px;background:linear-gradient(180deg,#3a3a3c,#1f1f21 60%,#5a4634)"></div>
</section>

<section class="section accessories">
  <h2 class="section-title" style="top:80px">Popular <em>Accessories</em></h2>
  <p class="section-lead" style="top:147px">Lorem ipsum dolor sit amet, consectetur adipiscing elit,<br>sed do eiusmod tempor incididunt ut labore et dolore magna aliqua quis ipsum suspendisse ultrices gravida.</p>
  <div class="acc-card" style="left:112px"><div class="acc-photo" role="img" aria-label="Clear glass pitcher"></div><span class="stars">★★★★☆</span><div class="acc-name">Whiskey Glasses</div><div class="acc-price">$20</div></div>
  <div class="acc-card" style="left:365px"><div class="acc-photo" role="img" aria-label="Ice cubes"></div><span class="stars">★★★★☆</span><div class="acc-name">Whiskey Ice Cubes</div><div class="acc-price">$20</div></div>
  <div class="acc-card" style="left:617px"><div class="acc-photo" role="img" aria-label="Leather bar stool"></div><span class="stars">★★★★☆</span><div class="acc-name">Decanter</div><div class="acc-price">$20</div></div>
  <div class="acc-card" style="left:869px"><div class="acc-photo" role="img" aria-label="Gold bar cart with glassware"></div><span class="stars">★★★★☆</span><div class="acc-name">Whiskey Glasses</div><div class="acc-price">$20</div></div>
  <a class="btn" style="left:531px;top:598px;width:137px;height:33px">View More</a>
</section>

<section class="section video">
  <div class="video-photo" role="img" aria-label="Backlit bar shelves lined with bottles above a wooden counter"></div>
  <h2>Whiskey Accessories – Enhance Every Sip</h2>
  <span class="play"><svg width="26" height="30" viewBox="0 0 26 30"><path d="M3 2l21 13L3 28z" fill="#111"/></svg></span>
</section>

<section class="section blog">
  <h2 class="section-title" style="top:80px">Latest <em>Blog</em></h2>
  <p class="section-lead" style="top:141px">Lorem ipsum dolor sit amet, consectetur adipiscing elit,<br>sed do eiusmod tempor incididunt ut labore et dolore magna aliqua quis ipsum suspendisse ultrices gravida.</p>
  <article class="post" style="left:110px"><div class="post-photo" role="img" aria-label="Living room with leather sofa and bookshelves" style="background:linear-gradient(90deg,#6a4a36,#b8a89a 55%,#a34a2a)"></div><div class="post-cat">Scotch Whisky</div><div class="post-title">Lorem ipsum dolor sit amet,<br>consectetur adipiscing elit, sed do</div><div class="post-meta">Nov 15, 2024 &nbsp;- &nbsp;0 Comments</div></article>
  <article class="post" style="left:450px"><div class="post-photo" role="img" aria-label="Long bar with lit bottle shelves and stools" style="background:linear-gradient(180deg,#2a1e16,#7a5030 45%,#1e1a18)"></div><div class="post-cat">Scotch Whisky</div><div class="post-title">Lorem ipsum dolor sit amet,<br>consectetur adipiscing elit, sed do</div><div class="post-meta">Nov 15, 2024 &nbsp;- &nbsp;0 Comments</div></article>
  <article class="post" style="left:789px"><div class="post-photo" role="img" aria-label="Warm wood lounge with curved booths" style="background:linear-gradient(180deg,#5a3220,#a9703f 50%,#6e4430)"></div><div class="post-cat">Scotch Whisky</div><div class="post-title">Lorem ipsum dolor sit amet,<br>consectetur adipiscing elit, sed do</div><div class="post-meta">Nov 15, 2024 &nbsp;- &nbsp;0 Comments</div></article>
</section>

<footer class="section site-footer">
  <div class="footer-badge">Bourbon<br>Lantern</div>
  <nav class="footer-nav">
    <a style="left:297px">Home</a>
    <a style="left:389px">About Us</a>
    <a style="left:507px">Shop</a>
    <a style="left:590px">Accessories</a>
    <a style="left:729px">Blog</a>
    <a style="left:806px">Contact Us</a>
  </nav>
  <div class="copyright">Copyright © 2024 Bourbon Lantern. All rights reserved.</div>
</footer>

</body>
</html>
```